Real Estate Entrepreneur needs a business card

I am a real estate entrepreneur, I buy houses for investment purposes, I act as a real estate agent representing buyers and sellers in residential home transactions, I am a contractor that does a wide range of home repairs and construction. I'd like a design that can stick with me through the years as my business grows and morphs to fit any niche I decide to pursue as markets change.

Target Market(s)

Anyone with interest that may be related to real estate.

Industry/Entity Type

Real Estate

Contact Information for Business Card

A card that stands out and doesn't put me in any one box. My business will evolve over time and I need a card that can stay relevant.

Colors

Designer to choose colors to be used in the design.

Requirements
Must have
• Character
Nice to have
• I'm open
Should not have
• Cliche houses and hammers

```html
<!DOCTYPE html>
<html lang="en">
<head>
<meta charset="UTF-8">
<title>Reid Hollow – Business Card</title>
<link href="https://fonts.googleapis.com/css2?family=Poppins:wght@300;400;600&display=swap" rel="stylesheet">
<style>
  :root {
    --backdrop: #1c1c1c;
    --card: #f3f3f1;
    --ink: #3a3a3a;
    --ink-soft: #6b6b6b;
    --gold: #c2a65a;
  }
  html, body {
    margin: 0;
    padding: 0;
    width: 1200px;
    height: 900px;
    overflow: hidden;
    background: var(--backdrop);
  }
  .canvas {
    width: 1200px;
    height: 900px;
    display: flex;
    align-items: center;
    justify-content: center;
  }
  .business-card {
    position: relative;
    width: 840px;
    height: 480px;
    background: var(--card);
    box-sizing: border-box;
    font-family: "Poppins", sans-serif;
    color: var(--ink);
  }
  .identity {
    position: absolute;
    left: 200px;
    top: 70px;
  }
  .brand-mark {
    display: block;
    margin: 0 0 18px 92px;
  }
  .brand-name {
    margin: 0;
    font-size: 40px;
    font-weight: 600;
    letter-spacing: 1px;
    line-height: 1.05;
    color: var(--ink);
  }
  .brand-role {
    margin: 4px 0 0 2px;
    font-size: 21px;
    font-weight: 300;
    letter-spacing: 1px;
    color: var(--ink-soft);
  }
  .divider {
    width: 16px;
    height: 2px;
    background: var(--ink);
    margin: 14px 0 12px 2px;
  }
  .contact-list {
    list-style: none;
    margin: 0;
    padding: 0 0 0 2px;
    font-size: 18px;
    font-weight: 400;
    line-height: 1.55;
    color: var(--ink);
  }
</style>
</head>
<body>
  <main class="canvas">
    <section class="business-card">
      <div class="identity">
        <svg class="brand-mark" width="110" height="110" viewBox="0 0 110 110" aria-hidden="true">
          <circle cx="55" cy="55" r="55" fill="var(--gold)"/>
        </svg>
        <h1 class="brand-name">REID HOLLOW</h1>
        <p class="brand-role">Real Estate Agent</p>
        <div class="divider"></div>
        <ul class="contact-list">
          <li>042-555-0143</li>
          <li>contact@reidhollow.com</li>
          <li>www.reidhollow.com</li>
        </ul>
      </div>
    </section>
  </main>
</body>
</html>
```